Stationery wanted for Brand New Law Firm

I need a stationery for a law firm that I am establishing. I am after letterhead (black & white and colour version, envelope, document folder, business cards and email signature
The firm will be a "modern" law firm providing commercial advice and transactional assistance to small to medium businesses (sales, purchases and leases of commercial property, business structuring advice, shareholders agreement etc).

Target Market(s)

Small to medium business owners in Sydney, Australia

Industry/Entity Type

Legal

Contact Information for Business Card

Rosalind Penhallow
Principal Lawyer
Penhallow Legal
PO Box 4829 Kellmont Plaza NSW 2187
[Phone No to be provided]
r@penhallowlegal.com.au
www.penhallowlegal.com.au
Tag line - "Expert legal advice for property and business owners"

Colors
ffffff
0555a3
ffc214

Requirements
Must have
• * Attached logo
* Letterhead have colour and black and white options. Other documents to be the same colour scheme as the attached logo.
* Modern, minimalistic feel
* Letterhead and email signature must include the following words:
"Liability limited by a scheme approved under Professional Standards Legislation."

```html
<!DOCTYPE html>
<html lang="en">
<head>
<meta charset="utf-8">
<title>Penhallow Legal Stationery</title>
<link rel="stylesheet" href="https://fonts.googleapis.com/css2?family=Lato:wght@300;400;700&family=Pinyon+Script&display=swap">
<style>
:root{
  --navy:#17194f;
  --gold:#c99a43;
  --paper:#f4f4f4;
  --paper-white:#f8f8f8;
  --stage:#e9e9e9;
  --ink:#3c3c44;
  --muted:#6b6b74;
  --rule:#c9c9cf;
}
*{box-sizing:border-box;margin:0;padding:0}
html,body{width:1200px;height:1019px;overflow:hidden}
body{background:var(--stage);font-family:'Lato',sans-serif;color:var(--ink);position:relative}
.sheet{position:absolute;background:var(--paper);box-shadow:0 2px 8px rgba(0,0,0,.12);overflow:hidden}
.band{position:absolute;left:0;bottom:0;width:100%;display:block}
.wordmark{position:absolute;text-align:center;color:var(--navy);font-weight:400;white-space:nowrap;line-height:1}
.wordmark .dot{display:block;margin:5px auto 0;border-radius:50%;background:var(--gold)}
.wordmark.on-dark{color:#fff}
.icon{display:inline-block;width:6px;height:6px;margin-right:4px;vertical-align:middle}

/* Letterhead */
.letterhead{left:157px;top:151px;width:436px;height:617px}
.letterhead .wordmark{left:30px;top:26px;font-size:21px}
.letterhead .wordmark .dot{width:7px;height:7px}
.letter-date,.letter-recipient,.letter-greeting,.letter-body,.letter-closing{position:absolute;left:46px;font-size:7.2px;line-height:10.4px;color:var(--ink)}
.letter-date{top:145px}
.letter-recipient{top:165px}
.letter-recipient strong{font-weight:700;color:#222}
.letter-greeting{top:217px}
.letter-body{top:238px;width:344px;text-align:justify}
.letter-body p{margin-bottom:10.4px}
.letter-closing{top:463px}
.signature{position:absolute;left:50px;top:477px;font-family:'Pinyon Script',cursive;font-size:15px;line-height:18px;color:#222}
.letter-footer{position:absolute;left:35px;top:543px;font-size:7.2px;line-height:8.9px;color:var(--muted);white-space:nowrap}
.liability{font-size:7.2px;line-height:8.9px;color:var(--muted);text-align:right;white-space:nowrap}
.liability strong{color:var(--ink);font-weight:700}
.letterhead .liability{position:absolute;right:38px;top:582px}

/* Business cards */
.card-front{left:625px;top:139px;width:228px;height:130px;background:var(--paper-white)}
.card-front .wordmark{left:0;width:100%;top:20px;font-size:13px}
.card-front .wordmark .dot{width:5px;height:5px;margin-top:4px}
.card-name{position:absolute;right:125px;top:75px;text-align:right;white-space:nowrap}
.card-name b{display:block;font-size:7px;line-height:8px;font-weight:700;color:var(--navy)}
.card-name span{display:block;font-size:5px;line-height:6px;color:var(--muted)}
.card-divider{position:absolute;left:114px;top:66px;width:1px;height:35px;background:var(--rule)}
.card-contact{position:absolute;left:126px;top:65px;font-size:5px;line-height:6.6px;color:var(--muted);white-space:nowrap}
.card-contact .gap{height:3px}
.card-contact .icon{width:4px;height:4px;margin-right:3px}
.card-tagline{position:absolute;left:0;width:100%;top:111px;text-align:center;font-size:5px;line-height:6px;color:var(--muted)}
.card-tagline b{color:var(--navy);font-weight:700}
.card-back{left:897px;top:139px;width:227px;height:130px;background:var(--navy)}
.card-back .wordmark{left:0;width:100%;top:42px;font-size:16px}
.card-back .wordmark .dot{width:6px;height:6px}
.card-back .liability{position:absolute;left:0;width:100%;top:103px;text-align:center;color:#d8d9e6;font-size:5px;line-height:6.4px}
.card-back .liability strong{color:#fff}

/* Envelopes */
.envelope{left:624px;width:502px;height:217px;background:var(--paper-white)}
.envelope.first{top:297px}
.envelope.second{top:552px}
.envelope .wordmark{left:40px;top:32px;font-size:17px}
.envelope .wordmark .dot{width:6px;height:6px}
.envelope-return{position:absolute;left:44px;top:80px;font-size:7.5px;line-height:9px;color:var(--muted);white-space:nowrap}
.envelope-window{position:absolute;left:301px;top:142px;width:145px;height:50px;border-radius:6px;border:1px solid #c4c4c4;background:linear-gradient(115deg,#c9c9c9 0%,#e4e4e4 45%,#cfcfcf 60%,#e9e9e9 100%)}

/* Email signature */
.email-signature{left:398px;top:793px;width:404px;height:130px;background:var(--paper-white)}
.email-signature .wordmark{left:18px;top:36px;font-size:19px}
.email-signature .wordmark .dot{width:6px;height:6px}
.social-links{position:absolute;left:57px;top:91px;display:flex;gap:3px}
.social-links span{width:11px;height:11px;border-radius:50%;background:var(--navy)}
.sig-name{position:absolute;left:172px;top:21px;white-space:nowrap}
.sig-name b{display:block;font-size:10.5px;line-height:12px;font-weight:700;color:var(--navy)}
.sig-name span{display:block;font-size:7px;line-height:9px;color:var(--muted)}
.sig-contact{position:absolute;top:50px;font-size:7px;line-height:8.8px;color:var(--muted);white-space:nowrap}
.sig-contact.primary{left:172px}
.sig-contact.office{left:279px}
.sig-rule{position:absolute;left:172px;top:82px;width:200px;height:1px;background:var(--rule)}
.email-signature .liability{position:absolute;left:172px;top:89px;text-align:left;font-size:7px;line-height:8.4px}
</style>
</head>
<body>

<svg width="0" height="0" style="position:absolute" aria-hidden="true">
  <defs>
    <symbol id="i-phone" viewBox="0 0 10 10"><path d="M2 1 L4 1 L4.6 3.2 L3.4 4 Q4.4 6 6 6.6 L6.8 5.4 L9 6 L9 8 Q9 9 8 9 Q1 8.6 1 2 Q1 1 2 1Z" fill="#17194f"/></symbol>
    <symbol id="i-mail" viewBox="0 0 10 10"><rect x="0.5" y="2" width="9" height="6" fill="#17194f"/><path d="M0.5 2 L5 5.5 L9.5 2" stroke="#fff" stroke-width="0.9" fill="none"/></symbol>
    <symbol id="i-web" viewBox="0 0 10 10"><circle cx="5" cy="5" r="4.3" fill="#17194f"/><path d="M0.8 5 H9.2 M5 0.8 V9.2 M5 0.8 Q2 5 5 9.2 M5 0.8 Q8 5 5 9.2" stroke="#fff" stroke-width="0.6" fill="none"/></symbol>
  </defs>
</svg>

<!-- Letterhead -->
<section class="sheet letterhead">
  <div class="wordmark">Penhallow Legal<span class="dot"></span></div>
  <p class="letter-date">01 January 2050</p>
  <p class="letter-recipient"><strong>Brightwell Trading Co.</strong><br>PO Box 3355 Ashcombe St<br>Sample City Country 3355</p>
  <p class="letter-greeting">Dear Daniel Marlowe,</p>
  <div class="letter-body">
    <p>Lorem ipsum dolor sit amet, consectetuer adipiscing elit, sed diam nonummy nibh euismod tincidunt ut laoreet dolore magna aliquam erat volutpat. Ut wisi enim ad minim veniam, quis nostrud exerci tation ullamcorper suscipit lobortis nisl ut aliquip ex ea commodo consequat. Duis dolore te feugait nulla facilisi. Nam liber tempor cum soluta nobis eleifend option congue nihil imperdiet doming id quod mazim placerat facer possim assum. Lorem ipsum dolor sit amet, consectetuer adipiscing elit, sed diam nonummy nibh euismod tincidunt ut laoreet dolore magna aliquam erat volutpat. Ut wisi enim ad minim veniam, quis nostrud exerci tation ullamcorper suscipit lobortis nisl ut aliquip ex ea commodo consequat.</p>
    <p>Consectetuer adipiscing elit, sed diam nonummy nibh euismod tincidunt ut laoreet dolore magna aliquam erat volutpat. Ut wisi enim ad minim veniam, quis nostrud exerci tation ullamcorper suscipit lobortis nisl ut aliquip ex ea commodo consequat. Consectetuer adipiscing elit, sed diam nonummy nibh euismod tincidunt ut laoreet dolore magna aliquam erat volutpat. Ut wisi enim ad minim veniam, quis nostrud exerci tation ullamcorper suscipit lobortis nisl ut aliquip ex ea commodo consequat.</p>
    <p>Consectetuer adipiscing elit, sed diam nonummy nibh euismod tincidunt ut laoreet dolore magna aliquam erat volutpat. Ut wisi enim ad minim veniam, quis nostrud exerci tation ullamcorper suscipit lobortis nisl ut aliquip ex ea commodo consequat. Consectetuer adipiscing elit, sed diam nonummy nibh euismod tincidunt ut laoreet dolore magna aliquam erat volutpat. Ut wisi enim ad minim veniam, quis nostrud exerci tation ullamcorper suscipit lobortis nisl ut aliquip ex ea commodo consequat.</p>
  </div>
  <p class="letter-closing">Sincerely Yours</p>
  <p class="signature">Thomas Edgar Whitby</p>
  <div class="letter-footer">
    Penhallow Legal<br>PO Box 4829<br>Kellmont Plaza NSW 2187<br>
    <svg class="icon"><use href="#i-phone"/></svg>(200) 555.0142<br>
    <svg class="icon"><use href="#i-mail"/></svg>info@penhallowlegal.com.au<br>
    <svg class="icon"><use href="#i-web"/></svg>www.penhallowlegal.com.au
  </div>
  <p class="liability">Liability limited by a scheme approved under<br><strong>Professional Standards Legislation</strong>.</p>
  <svg class="band" height="6" viewBox="0 0 100 6" preserveAspectRatio="none"><rect width="100" height="6" fill="var(--gold)"/><polygon points="0,0 50.5,0 49.5,6 0,6" fill="var(--navy)"/></svg>
</section>

<!-- Business card front -->
<section class="sheet card-front">
  <div class="wordmark">Penhallow Legal<span class="dot"></span></div>
  <div class="card-name"><b>Rosalind Penhallow</b><span>Principal Lawyer</span></div>
  <div class="card-divider"></div>
  <div class="card-contact">
    PO Box 4829<br>Kellmont Plaza NSW 2187
    <div class="gap"></div>
    <svg class="icon"><use href="#i-phone"/></svg>(200) 555.0142<br>
    <svg class="icon"><use href="#i-mail"/></svg>r@penhallowlegal.com.au<br>
    <svg class="icon"><use href="#i-web"/></svg>www.penhallowlegal.com.au
  </div>
  <p class="card-tagline">Expert Legal Advice for <b>Property &amp; Business Owners</b></p>
  <svg class="band" height="5" viewBox="0 0 100 5" preserveAspectRatio="none"><rect width="100" height="5" fill="var(--gold)"/><polygon points="0,0 50.5,0 49.5,5 0,5" fill="var(--navy)"/></svg>
</section>

<!-- Business card back -->
<section class="sheet card-back">
  <div class="wordmark on-dark">Penhallow Legal<span class="dot"></span></div>
  <p class="liability">Liability limited by a scheme approved under<br><strong>Professional Standards Legislation</strong></p>
</section>

<!-- Envelopes -->
<section class="sheet envelope first">
  <div class="wordmark">Penhallow Legal<span class="dot"></span></div>
  <p class="envelope-return">Penhallow Legal<br>PO Box 4829<br>Kellmont Plaza NSW 2187</p>
  <div class="envelope-window"></div>
  <svg class="band" height="8" viewBox="0 0 100 8" preserveAspectRatio="none"><rect width="100" height="8" fill="var(--navy)"/><polygon points="0,0 9.4,0 8.6,8 0,8" fill="var(--gold)"/></svg>
</section>

<section class="sheet envelope second">
  <div class="wordmark">Penhallow Legal<span class="dot"></span></div>
  <p class="envelope-return">Penhallow Legal<br>PO Box 4829<br>Kellmont Plaza NSW 2187</p>
  <div class="envelope-window"></div>
  <svg class="band" height="8" viewBox="0 0 100 8" preserveAspectRatio="none"><rect width="100" height="8" fill="var(--navy)"/><polygon points="0,0 9.4,0 8.6,8 0,8" fill="var(--gold)"/></svg>
</section>

<!-- Email signature -->
<section class="sheet email-signature">
  <div class="wordmark">Penhallow Legal<span class="dot"></span></div>
  <div class="social-links" aria-label="Social links"><span></span><span></span><span></span><span></span></div>
  <div class="sig-name"><b>Rosalind Penhallow</b><span>Principal Lawyer</span></div>
  <div class="sig-contact primary">
    <svg class="icon"><use href="#i-phone"/></svg>(200) 555.0142<br>
    <svg class="icon"><use href="#i-mail"/></svg>r@penhallowlegal.com.au<br>
    <svg class="icon"><use href="#i-web"/></svg>www.penhallowlegal.com.au
  </div>
  <div class="sig-contact office">Penhallow Legal<br>PO Box 4829<br>Kellmont Plaza NSW 2187</div>
  <div class="sig-rule"></div>
  <p class="liability">Liability limited by a scheme approved under<br><strong>Professional Standards Legislation</strong>.</p>
  <svg class="band" height="6" viewBox="0 0 100 6" preserveAspectRatio="none"><rect width="100" height="6" fill="var(--gold)"/><polygon points="0,0 50.5,0 49.5,6 0,6" fill="var(--navy)"/></svg>
</section>

</body>
</html>
```